Brelvanhomes42.com needs a website.

I'm looking for a website that offeres education and courses about the QZ home loan. This will teach people what they need to know about using the QZ loan. I need a website design that will allow the use of video, have sections to educate about the myths out there, use blue and red which are patriotic colors.

```html
<!DOCTYPE html>
<html lang="en">
<head>
<meta charset="utf-8">
<title>About Us – Brelvanhomes42.com</title>
<link href="https://fonts.googleapis.com/css2?family=Lexend:wght@400;500;600&family=Roboto:wght@400;500;700&display=swap" rel="stylesheet">
<style>
:root{
  --navy:#13255f;
  --blue:#0d63d4;
  --blue-light:#2b7be3;
  --red:#d62839;
  --ink:#13255f;
  --text:#555b6e;
  --line:#dfe3ec;
  --soft:#f5f5f5;
  --white:#fff;
  --amber:#f0a92b;
}
*{box-sizing:border-box;margin:0;padding:0}
html,body{width:1200px;height:3009px;overflow:hidden}
body{position:relative;background:var(--white);font-family:'Roboto',sans-serif;color:var(--text)}
.abs{position:absolute}
h1,h2,h3,h4,.lex{font-family:'Lexend',sans-serif;color:var(--ink);font-weight:500}

/* top bar */
.topbar{left:0;top:0;width:1200px;height:38px;background:var(--navy);color:#fff;font-size:13px;border-bottom:3px solid var(--red)}
.topbar .item{position:absolute;top:11px;display:flex;align-items:center;gap:7px}
.topbar .sep{position:absolute;top:10px;width:1px;height:15px;background:#fff}
.social-dot{position:absolute;top:13px;width:11px;height:11px;border-radius:50%;background:#fff}

/* header */
.header{left:0;top:38px;width:1200px;height:77px;background:#fff;box-shadow:0 1px 0 #eef0f5}
.logo{left:12px;top:0;width:163px;height:100px;background:var(--blue);border-radius:0 0 12px 12px;display:flex;align-items:center;justify-content:center;gap:7px;color:#fff;font-family:'Lexend',sans-serif;font-size:13px;font-weight:400}
.logo .mark{width:11px;height:11px;background:var(--red);border-radius:50%}
.nav a{position:absolute;top:68px;font-size:15px;color:#1b2340;text-decoration:none;font-weight:500}
.nav a.active{color:var(--blue)}

/* hero */
.hero{left:0;top:115px;width:1200px;height:251px;background:linear-gradient(90deg,#2a3f7c,#344b8c 45%,#24386f);text-align:center}
.hero h1{position:absolute;top:88px;width:100%;font-size:40px;font-weight:600;color:#fff}
.crumb{position:absolute;top:147px;width:100%;font-size:13px;color:#fff;font-weight:500}
.crumb span{color:#4d9af5}

/* about */
.eyebrow{font-size:14px;color:var(--red);font-weight:500}
.h-big{font-size:40px;line-height:51px;font-weight:500}
.para{font-size:13px;line-height:20.5px}
.feat-title{font-size:17px;font-weight:500}
.btn{display:flex;align-items:center;justify-content:center;gap:10px;background:var(--blue);color:#fff;font-size:13px;font-weight:700;text-transform:uppercase;border-bottom:3px solid var(--red)}
.photo{position:absolute}

/* stats */
.stat-band{left:0;top:1217px;width:1200px;height:517px;background:var(--soft)}
.stats{left:104px;top:1061px;width:992px;height:281px;background:var(--navy);background-image:radial-gradient(rgba(255,255,255,.05) 1.5px,transparent 1.5px);background-size:18px 18px;border-bottom:4px solid var(--red)}
.stat{position:absolute;top:63px;color:#fff}
.stat .ic{width:62px;height:62px;background:#fff;border-radius:4px;display:flex;align-items:center;justify-content:center}
.stat .num{font-family:'Lexend',sans-serif;font-size:38px;font-weight:600;margin-top:20px;line-height:44px}
.stat .lbl{font-size:15px;margin-top:4px;font-weight:400}

/* instructor */
.join h2{position:absolute;top:1435px;width:1200px;text-align:center;font-size:40px;font-weight:500}
.join .para{position:absolute;top:1508px;left:300px;width:600px;text-align:center}
.tilt{position:absolute;width:175px;height:175px;border-radius:30px;transform:rotate(22deg);border:6px solid #fff;box-shadow:0 0 0 1px #e3e3e3}

/* myths & facts accordion */
.acc{position:absolute;left:143px;width:445px;border:1px solid var(--line);background:#fff}
.acc.open{border-left:3px solid var(--red)}
.acc .q{position:absolute;left:23px;top:19px;font-family:'Lexend',sans-serif;font-size:14px;color:var(--ink);font-weight:500}
.acc .q b{color:var(--red);font-weight:500}
.acc .tog{position:absolute;right:22px;top:18px}
.acc .a{position:absolute;left:23px;top:57px;width:400px;font-size:12.5px;line-height:20.5px}
.card-blue{left:680px;top:1931px;width:180px;height:162px;background:var(--blue);color:#fff;padding:30px 26px;font-family:'Lexend',sans-serif;font-size:15px;line-height:23px}

/* partners */
.partner{position:absolute;top:2441px;display:flex;align-items:center;gap:8px;font-family:'Lexend',sans-serif;font-size:22px;font-weight:600;color:#6c7080}
.partner .dot{width:22px;height:22px;border-radius:50%;background:#9aa0ad}

/* footer */
.footer{left:0;top:2585px;width:1200px;height:424px;background:var(--navy);color:#fff;border-top:4px solid var(--red)}
.footer h4{position:absolute;top:74px;color:#fff;font-size:18px;font-weight:500}
.flist{position:absolute;top:117px;list-style:none;font-size:12.5px}
.flist li{height:34.5px}
.ftext{position:absolute;left:143px;top:117px;width:200px;font-size:12.5px;line-height:20.5px}
.finfo{position:absolute;left:846px;display:flex;gap:10px;font-size:12.5px;line-height:22px}
.fsocial{position:absolute;top:255px;width:30px;height:30px;border-radius:50%;background:#24387a;display:flex;align-items:center;justify-content:center}
.fsocial i{width:8px;height:8px;border-radius:50%;background:#fff;display:block}
.divider{position:absolute;left:143px;top:356px;width:914px;height:1px;background:#2b3d78}
.copy{position:absolute;top:383px;font-size:12.5px}
</style>
</head>
<body>

<!-- top bar -->
<div class="abs topbar">
  <div class="item" style="left:230px">
    <svg width="12" height="14" viewBox="0 0 12 14"><path d="M6 1a4.5 4.5 0 0 0-4.5 4.5C1.5 9 6 13 6 13s4.5-4 4.5-7.5A4.5 4.5 0 0 0 6 1z" fill="none" stroke="var(--amber)" stroke-width="1.5"/><circle cx="6" cy="5.5" r="1.6" fill="var(--amber)"/></svg>
    Address : 14 Harlow Plaza, Marlton
  </div>
  <div class="sep" style="left:468px"></div>
  <div class="item" style="left:492px">
    <svg width="14" height="14" viewBox="0 0 14 14"><circle cx="7" cy="7" r="5.8" fill="none" stroke="var(--amber)" stroke-width="1.5"/><path d="M7 4v3.3l2 1.3" fill="none" stroke="var(--amber)" stroke-width="1.5"/></svg>
    Working : Monday - Friday, 9:Am - 5:Pm
  </div>
  <div class="item" style="left:936px">
    <svg width="13" height="14" viewBox="0 0 13 14"><circle cx="6.5" cy="4.5" r="3" fill="none" stroke="var(--amber)" stroke-width="1.5"/><path d="M1 13c.5-3 3-4.5 5.5-4.5S11.5 10 12 13" fill="none" stroke="var(--amber)" stroke-width="1.5"/></svg>
    Login/ Register
  </div>
  <div class="sep" style="left:1065px"></div>
  <span class="social-dot" style="left:1093px"></span>
  <span class="social-dot" style="left:1120px"></span>
  <span class="social-dot" style="left:1147px"></span>
  <span class="social-dot" style="left:1174px"></span>
</div>

<!-- header -->
<div class="abs header"></div>
<div class="abs logo"><span class="mark"></span>Brelvanhomes42.com</div>
<nav class="nav">
  <a style="left:372px">Home</a>
  <a class="active" style="left:444px">About Us</a>
  <a style="left:536px">Courses</a>
  <a style="left:621px">Video Library</a>
  <a style="left:742px">Blog</a>
  <a style="left:804px">Contact</a>
</nav>
<svg class="abs" style="left:1075px;top:68px" width="18" height="18" viewBox="0 0 18 18"><circle cx="7.5" cy="7.5" r="6" fill="none" stroke="#1b2340" stroke-width="1.8"/><path d="M12 12l5 5" stroke="#1b2340" stroke-width="1.8"/></svg>
<svg class="abs" style="left:1116px;top:66px" width="20" height="22" viewBox="0 0 20 22"><path d="M3 7h14l-1 13H4z" fill="none" stroke="#1b2340" stroke-width="1.7"/><path d="M7 9V5a3 3 0 0 1 6 0v4" fill="none" stroke="#1b2340" stroke-width="1.7"/></svg>
<div class="abs" style="left:1131px;top:63px;width:14px;height:14px;border-radius:50%;background:var(--red);color:#fff;font-size:9px;text-align:center;line-height:14px">0</div>
<svg class="abs" style="left:1168px;top:70px" width="20" height="14" viewBox="0 0 20 14"><path d="M0 1h20M5 7h15M0 13h20" stroke="var(--blue)" stroke-width="1.8"/></svg>

<!-- hero -->
<section class="abs hero" role="img" aria-label="Students studying together, tinted navy banner">
  <h1>About Us</h1>
  <div class="crumb">Home &nbsp;/&nbsp; <span>About Us</span></div>
</section>

<!-- about -->
<div class="abs eyebrow" style="left:143px;top:463px">About Company</div>
<h2 class="abs h-big" style="left:143px;top:492px;width:470px">We Are Truly Teaching You QZ Mortgage</h2>
<p class="abs para" style="left:143px;top:615px;width:425px">Aliquam Mauris Leo, Mollis Tempus Semper In, Fringilla Ac Libero. Curabitur Id Venenatis Leo. Aenean Id Venenatis Lectus, Ac Semper Lacus. Vestibulum Malesuada Libero</p>

<svg class="abs" style="left:143px;top:702px" width="40" height="40" viewBox="0 0 40 40" fill="none" stroke="var(--blue)" stroke-width="1.4"><circle cx="13" cy="12" r="5"/><path d="M4 34c0-7 4-12 9-12s9 5 9 12"/><rect x="20" y="22" width="16" height="12"/><circle cx="31" cy="7" r="5" stroke="var(--red)"/><path d="M31 4v3l2 1" stroke="var(--red)"/></svg>
<h3 class="abs feat-title" style="left:205px;top:704px">Realtime Learning</h3>
<p class="abs para" style="left:205px;top:736px;width:320px">Aliquam Mauris Leo, Mollis Tempus Semper In, Fringilla Ac Libero. Curabitur Id Venenatis</p>

<svg class="abs" style="left:143px;top:802px" width="40" height="34" viewBox="0 0 40 34" fill="none" stroke="var(--blue)" stroke-width="1.4"><rect x="1" y="3" width="30" height="26" rx="2"/><path d="M1 9h30"/><circle cx="15" cy="19" r="6" stroke="var(--red)"/><path d="M13 16v6l5-3z" stroke="var(--red)"/><rect x="30" y="18" width="9" height="12" rx="1.5"/></svg>
<h3 class="abs feat-title" style="left:205px;top:802px">Educational Video</h3>
<p class="abs para" style="left:205px;top:834px;width:320px">Aliquam Mauris Leo, Mollis Tempus Semper In, Fringilla Ac Libero. Curabitur Id Venenatis</p>

<div class="abs btn" style="left:143px;top:912px;width:169px;height:47px">More About
  <svg width="16" height="10" viewBox="0 0 16 10"><path d="M0 5h14M10 1l4 4-4 4" fill="none" stroke="#fff" stroke-width="1.6"/></svg></div>
<div class="abs" style="left:353px;top:912px;width:44px;height:44px;border-radius:50%;background:#eef3fb"></div>
<svg class="abs" style="left:362px;top:922px" width="30" height="30" viewBox="0 0 30 30" fill="none" stroke="var(--blue)" stroke-width="1.4"><path d="M5 4l5-1 3 6-3 2c1.5 3.5 4 6 7.5 7.5l2-3 6 3-1 5C14 24 6 16 5 4z"/><path d="M18 4a8 8 0 0 1 8 8M18 8a4 4 0 0 1 4 4" stroke="var(--red)"/></svg>
<div class="abs lex" style="left:410px;top:914px;font-size:13px;color:var(--ink)">Need Any Help</div>
<div class="abs lex" style="left:410px;top:936px;font-size:17px;font-weight:500;color:var(--ink)">(+1) 555 014 270</div>

<div class="photo" role="img" aria-label="Hands sorting colourful document tabs" style="left:781px;top:449px;width:241px;height:279px;background:linear-gradient(160deg,#dfe5ee,#e9c9a5 55%,#c9b3a2)"></div>
<div class="photo" role="img" aria-label="Soldier in camouflage hugging his daughter" style="left:601px;top:577px;width:249px;height:272px;background:#fff;padding:8px"><div style="width:100%;height:100%;background:linear-gradient(150deg,#b7a88a,#8d7b5e 50%,#5d5040)"></div></div>
<div class="photo" role="img" aria-label="Model house on a desk beside a person signing papers" style="left:736px;top:757px;width:327px;height:210px;background:linear-gradient(120deg,#f0ede8,#c6a18a 55%,#8a6a55)"></div>

<!-- stats -->
<div class="abs stat-band"></div>
<div class="abs stats">
  <div class="stat" style="left:72px">
    <div class="ic"><svg width="34" height="30" viewBox="0 0 34 30" fill="none" stroke="var(--blue)" stroke-width="1.5"><rect x="2" y="2" width="30" height="20"/><path d="M12 28h10M17 22v6M9 10l8-4 8 4-8 4z"/></svg></div>
    <div class="num">120k+</div><div class="lbl">Total Courses</div>
  </div>
  <div class="stat" style="left:318px">
    <div class="ic"><svg width="32" height="32" viewBox="0 0 32 32" fill="none" stroke="var(--red)" stroke-width="1.5"><rect x="12" y="3" width="18" height="14"/><circle cx="9" cy="12" r="4"/><path d="M2 29c0-6 3-10 7-10s7 4 7 10"/></svg></div>
    <div class="num">120+</div><div class="lbl">Expert Instructor</div>
  </div>
  <div class="stat" style="left:568px">
    <div class="ic"><svg width="30" height="32" viewBox="0 0 30 32" fill="none" stroke="var(--blue)" stroke-width="1.5"><circle cx="15" cy="9" r="5"/><path d="M4 30c0-7 5-12 11-12s11 5 11 12z"/><rect x="10" y="22" width="10" height="6"/></svg></div>
    <div class="num">119k+</div><div class="lbl">Happy Students</div>
  </div>
  <div class="stat" style="left:818px">
    <div class="ic"><svg width="28" height="32" viewBox="0 0 28 32" fill="none" stroke="var(--red)" stroke-width="1.5"><circle cx="14" cy="12" r="9"/><path d="M14 7l1.6 3.3 3.6.5-2.6 2.5.6 3.6L14 15.2 10.8 17l.6-3.6-2.6-2.5 3.6-.5z"/><path d="M9 20l-3 10 5-2 3 3M19 20l3 10-5-2-3 3"/></svg></div>
    <div class="num">119+</div><div class="lbl">National Award</div>
  </div>
</div>

<!-- become an instructor -->
<section class="join">
  <div class="tilt" role="img" aria-label="Portrait of a female instructor at a chalkboard" style="left:-4px;top:1445px;background:linear-gradient(140deg,#4a4f55,#8a6a55)"></div>
  <div class="tilt" role="img" aria-label="Portrait of a smiling male instructor at a chalkboard" style="left:1027px;top:1445px;background:linear-gradient(140deg,#4f6a5e,#3a3f48)"></div>
  <h2>Become An Instructor Join With Us</h2>
  <p class="para">Aliquam Mauris Leo, Mollis Tempus Semper In, Fringilla Ac Libero. Curabitur Id Venenatis Leo. Aenean Id Venenatis Lectus, Ac Semper Lacus. Vestibulum Malesuada</p>
  <div class="abs btn" style="left:513px;top:1593px;width:170px;height:47px">Join With Us
    <svg width="16" height="10" viewBox="0 0 16 10"><path d="M0 5h14M10 1l4 4-4 4" fill="none" stroke="#fff" stroke-width="1.6"/></svg></div>
</section>

<!-- myths vs facts -->
<div class="abs eyebrow" style="left:143px;top:1830px">Myths Vs Facts</div>
<h2 class="abs h-big" style="left:143px;top:1861px;width:480px">We Give You Knowledge With Ease</h2>

<div class="acc" style="top:1994px;height:54px">
  <div class="q"><b>Myth 01.</b> You Can Only Use A QZ Loan Once?</div>
  <svg class="tog" width="16" height="16" viewBox="0 0 16 16"><path d="M8 0v16M0 8h16" stroke="var(--ink)" stroke-width="1.6"/></svg>
</div>
<div class="acc open" style="top:2064px;height:156px">
  <div class="q"><b>Myth 02.</b> A QZ Loan Needs A Down Payment?</div>
  <svg class="tog" width="16" height="16" viewBox="0 0 16 16"><path d="M0 8h16" stroke="var(--red)" stroke-width="1.6"/></svg>
  <p class="a">Aliquam Mauris Leo, Mollis Tempus Semper In, Fringilla Ac Libero. Curabitur Id Venenatis Leo. Aenean Id Venenatis Lectus, Ac Semper Lacus. Vestibulum Malesuada Libero Eget Vulputate Scelerisque. Cras Congue Urna Id Nulla Mattis,</p>
</div>
<div class="acc" style="top:2237px;height:54px">
  <div class="q"><b>Myth 03.</b> QZ Loans Always Close Slowly?</div>
  <svg class="tog" width="16" height="16" viewBox="0 0 16 16"><path d="M8 0v16M0 8h16" stroke="var(--ink)" stroke-width="1.6"/></svg>
</div>

<div class="photo" role="img" aria-label="Teacher helping a student write in a notebook" style="left:823px;top:1828px;width:288px;height:272px;background:linear-gradient(130deg,#e9e2d6,#a7896f 55%,#d8d0c6)"></div>
<div class="abs card-blue">120,20+ Students Join With Us
  <svg style="display:block;margin-top:17px" width="38" height="38" viewBox="0 0 38 38"><circle cx="19" cy="19" r="17.5" fill="none" stroke="#fff" stroke-width="2"/><circle cx="19" cy="19" r="14" fill="var(--red)"/><path d="M19 13v12M13 19h12" stroke="#fff" stroke-width="1.6"/></svg>
</div>
<div class="photo" role="img" aria-label="Three smiling students gathered around a laptop" style="left:690px;top:2116px;width:366px;height:210px;background:linear-gradient(120deg,#5a4b42,#a27a62 45%,#c95a4a 75%,#b7aaa0)"></div>

<!-- partners -->
<div class="partner" style="left:143px"><span class="dot"></span>Norvale</div>
<div class="partner" style="left:341px"><span class="dot"></span>Castwell</div>
<div class="partner" style="left:538px"><span class="dot"></span>Pemberly</div>
<div class="partner" style="left:736px"><span class="dot"></span>Trivant</div>
<div class="partner" style="left:932px"><span class="dot"></span>Oskara</div>

<!-- footer -->
<footer class="abs footer">
  <h4 style="left:143px">Get Started</h4>
  <h4 style="left:377px">Our Courses</h4>
  <h4 style="left:611px">Company</h4>
  <h4 style="left:846px">Infomation</h4>

  <p class="ftext">Integer Gravida Posuere Lacus Et Suscipit. Pellentesque Sed Ipsum Sollicitudin, Fermentum Nibh Elementum, Dignissim Leo. In Hac Habitasse Platea Dictumst.</p>
  <div class="abs" style="left:143px;top:240px;width:163px;height:44px;background:#fff;color:#8a8f9c;font-size:12.5px;padding:14px 20px">Email Address</div>
  <div class="abs" style="left:306px;top:240px;width:47px;height:44px;background:var(--red);display:flex;align-items:center;justify-content:center">
    <svg width="14" height="16" viewBox="0 0 14 16"><path d="M13 1L1 8l5 1 1 6z" fill="#fff"/></svg></div>

  <ul class="flist" style="left:377px">
    <li>Loan Basics</li><li>Eligibility Criteria</li><li>QZ Appraisals / LAPP</li><li>Credit Underwriting</li><li>Loan Processing Steps</li>
  </ul>
  <ul class="flist" style="left:611px">
    <li>About Us</li><li>Become An Instructor</li><li>Student Registration</li><li>FAQs</li><li>Contact Us</li>
  </ul>

  <div class="finfo" style="top:114px">
    <svg width="20" height="18" viewBox="0 0 20 18" fill="none" stroke="var(--blue-light)" stroke-width="1.4"><path d="M2 2l4-1 2 4-2 2c1 2.5 3 4.5 5.5 5.5l2-2 4 2-1 4C8 16 3 11 2 2z"/></svg>
    <span>(+1) 555 014 270</span></div>
  <div class="finfo" style="top:146px">
    <svg width="20" height="18" viewBox="0 0 20 18" fill="none" stroke="var(--blue-light)" stroke-width="1.4"><rect x="1" y="3" width="18" height="13"/><path d="M1 3l9 7 9-7"/></svg>
    <span>info@Brelvanhomes42.com</span></div>
  <div class="finfo" style="top:178px">
    <svg width="20" height="18" viewBox="0 0 20 18" fill="none" stroke="var(--blue-light)" stroke-width="1.4"><path d="M10 1a6 6 0 0 0-6 6c0 4.5 6 10 6 10s6-5.5 6-10a6 6 0 0 0-6-6z"/><circle cx="10" cy="7" r="2"/></svg>
    <span>48 Fenwick Row, Marlton,<br>United States</span></div>
  <span class="fsocial" style="left:846px"><i></i></span>
  <span class="fsocial" style="left:886px"><i></i></span>
  <span class="fsocial" style="left:926px"><i></i></span>
  <span class="fsocial" style="left:966px"><i></i></span>

  <div class="abs" style="left:1149px;top:320px;width:38px;height:38px;background:var(--blue);display:flex;align-items:center;justify-content:center">
    <svg width="12" height="8" viewBox="0 0 12 8"><path d="M1 7l5-5 5 5" fill="none" stroke="#fff" stroke-width="1.6"/></svg></div>

  <div class="divider"></div>
  <div class="copy" style="left:143px">Copyright © 2023 Brelvanhomes42. All Rights Reserved.</div>
  <div class="copy" style="left:876px">Support &nbsp;&nbsp;&nbsp;|&nbsp;&nbsp;&nbsp; Privacy &nbsp;&nbsp;&nbsp;|&nbsp;&nbsp;&nbsp; Policy</div>
</footer>

</body>
</html>
```